Power Point Template Kalmora sustainability consulting

Please note:
We are not looking for new design proposals anymore since we've already received templetes from two designers that we really like. We are currently discussing possible changes with them and will make a final decision soon. Thank you very much.

(find english description below)
We are a small German start-up that offers sustainability consulting. For presentations of results, our company presentation, proposals, lectures, etc., we need a PowerPoint template that matches our logo. We come from classic management consulting / strategy consulting and also deal with facts and figures in sustainability consulting. Therefore, the template should not be too fancy and should not only consist of photos. But it shouldn't be a completely sober template either. Our logo with the green leaves for sustainability (three leaves for KALmora) and the white bar chart (with the dynamic swing upwards) reflects our attitude well, where we see ourselves on the range from playful to sober and classic to modern.

It might be nice for the template to include the shape of one of the leaves (from the logo). Also, the logo should appear in a corner of each slide. The colors from the logo (see appendix) should be partially reflected in the presentation. We can also imagine a gold-brown tone (see website www.kalmora-consulting.example) or a coral tone as a contrast. (Attention - the website is not final yet).

For a first suggestion, it is sufficient to suggest three to four slides (cover sheet, chapter/separation slide, text slide, data slide). We will then mark drafts that we like. In total, we would then need about 6-10 more slide templates, e.g. about us, team, slide for a statement, 2-3 data charts (pie, bar, column), top 3 - 5 list, timeline, contact (more slides are welcome ).

We are a small German start-up offering sustainability consulting. We need a power point template for result presentations, our company presentation, proposals, lectures etc. The template should be aligned with our logo. Our background lies in classic management consulting / strategy consulting and we also deal with facts and figures in sustainability consulting. Therefore, the template should not be too playful and not only consist of photos. But it should also not be a completely clear template. Our logo with the green leaves for sustainability (three leaves for KALmora) and the white bar chart (with the dynamic upward swing) reflects our attitude well, where we see ourselves on the range from playful to down-to-earth and classic to modern .

For the template, it might be nice to incorporate the shape of one of the leaves (from the logo). Also, the logo should show up in one corner on each slide. Some of the colors from the logo (see attachment) should be reflected in the presentation. We could also think of a gold-brown tone (see website www.kalmora-consulting.example) or a coral tone for contrast. (Attention - the website is not final yet).

For a first proposal it is quite sufficient to suggest us three to four slides (cover page, chapter/separation slide, text slide, data slide). We will then mark the drafts that we like. In total we would need about 6-10 more slide templates, eg About us, Team, slide for a statement, 2-3 data charts (pie, bar, column), Top 3 - 5 List, Timeline, Contact (more slides are welcome).

Target Market(s)

Corporations, large companies and SMEs

Industry/Entity Type

Unternehmensberatung, Nachhaltigkeitsberatung

Font styles to use
Sans Serif
Other font styles liked:
• Calibri

Colors
00AB8E
00BBA5
67D7C9
C6EFE9
E9F9F6

Requirements
Must have
• see description (e.g. the colors of our logo)
Nice to have
• see description (e.g. elements of the logo included)
Should not have
• see description

```html
<!DOCTYPE html>
<html lang="en">
<head>
<meta charset="utf-8">
<title>Kalmora Sustainability Consulting – Slide Template</title>
<link href="https://fonts.googleapis.com/css2?family=Montserrat:wght@600;700;800&family=Mulish:wght@400;600;700&display=swap" rel="stylesheet">
<style>
  :root {
    --canvas: #7e8184;
    --white: #ffffff;
    --ink: #1c1c1c;
    --body: #3a3a3a;
    --leaf-green: #4f8a22;
    --leaf-light: #8cc63f;
    --leaf-pale: #b9d89a;
    --sand: #e6e2c9;
    --gold: #b59b4c;
    --grid: #e4e4e4;
    --axis: #9a9a9a;
    --ring: #7be35a;
    --ring-soft: #c9f3b8;
    --jan-a: #f2b90f; --jan-b: #f3dc7a;
    --feb-a: #ea4a1f; --feb-b: #f0a07f;
    --mar-a: #4b1a8a; --mar-b: #6c4f94;
    --apr-a: #3ab0c8; --apr-b: #6fbfd0;
    --head: "Montserrat", Arial, sans-serif;
    --text: "Mulish", Arial, sans-serif;
  }
  * { margin: 0; padding: 0; box-sizing: border-box; }
  html, body { width: 1200px; height: 3914px; overflow: hidden; }
  body { background: var(--canvas); position: relative; font-family: var(--text); color: var(--body); }

  .slide { position: absolute; left: 114px; width: 1002px; height: 562px; overflow: hidden; background: var(--white); }
  .slide--cover { top: 100px; }
  .slide--about { top: 726px; }
  .slide--team { top: 1352px; background: var(--sand); }
  .slide--chart { top: 1976px; }
  .slide--timeline { top: 2602px; }
  .slide--contact { top: 3228px; }

  .abs { position: absolute; }
  .photo { position: absolute; }

  .brand { position: absolute; display: flex; align-items: center; gap: 10px; }
  .brand__dot { width: 30px; height: 30px; border-radius: 50%; background: var(--leaf-green); flex: none; }
  .brand__name { font-family: var(--text); font-weight: 600; color: var(--leaf-green); font-size: 30px; line-height: 1; }
  .brand__tag { font-family: var(--text); font-size: 10.5px; letter-spacing: 0.3px; color: #5c6a4c; }

  .slide-title { position: absolute; display: flex; align-items: center; gap: 14px; font-family: var(--head); font-weight: 800; font-size: 21px; color: var(--ink); letter-spacing: 0.3px; }
  .slide-title .brand__dot { width: 26px; height: 26px; }

  /* cover */
  .cover__photo { inset: 0; background: linear-gradient(100deg, #e6e4e1 0%, #eeece8 35%, #d9cbbf 55%, #c7b4a4 70%, #a9b9cc 85%, #dcdcdc 100%); }
  .cover__headline { left: 53px; top: 190px; font-family: var(--head); font-weight: 800; font-size: 33px; line-height: 39px; color: var(--ink); letter-spacing: 0.5px; }
  .cover__brand { left: 20px; top: 22px; flex-direction: column; align-items: flex-start; gap: 2px; }
  .cover__brand .brand__row { display: flex; align-items: center; gap: 10px; }

  /* about */
  .about__panel { left: 0; top: 0; width: 447px; height: 334px; background: var(--leaf-green); }
  .about__text { right: 0; width: 311px; left: 0; top: 92px; text-align: right; color: var(--white); font-weight: 600; font-size: 15.5px; line-height: 25px; }
  .about__title { right: 31px; top: 30px; }
  .about__photo { left: 386px; top: 108px; width: 585px; height: 388px; background: linear-gradient(90deg, #9c9a97 0%, #8a8886 40%, #7e7c79 70%, #9a9895 100%); }
  .about__accent { left: -60px; top: 430px; width: 220px; height: 220px; border-radius: 50%; background: var(--leaf-pale); opacity: 0.55; }

  /* team */
  .team__title { left: 61px; top: 43px; }
  .team-card { position: absolute; top: 135px; width: 277px; height: 351px; background: var(--white); text-align: center; }
  .team-card__photo { position: relative; width: 100%; height: 249px; }
  .team-card__name { margin-top: 24px; font-family: var(--head); font-weight: 700; font-size: 13px; color: var(--ink); }
  .team-card__role { margin-top: 8px; font-size: 14px; color: var(--body); }

  /* chart */
  .chart__title { left: 40px; top: 47px; }
  .chart__heading { left: 40px; top: 150px; width: 300px; font-family: var(--head); font-weight: 800; font-size: 22px; line-height: 33px; color: var(--ink); }
  .chart__copy { left: 42px; top: 237px; width: 262px; font-size: 12.3px; line-height: 18.4px; color: var(--body); }
  .chart__svg { left: 0; top: 0; }

  /* timeline */
  .timeline__title { left: 24px; top: 26px; }
  .timeline__svg { left: 0; top: 0; }
  .step { position: absolute; width: 196px; text-align: center; }
  .step__label { font-family: var(--head); font-weight: 700; font-size: 11px; color: var(--ink); }
  .step__copy { margin-top: 14px; font-size: 10.4px; line-height: 12.6px; color: var(--body); }

  /* contact */
  .contact__photo { left: 0; top: 0; width: 547px; height: 562px; background: linear-gradient(160deg, #6e7f8f 0%, #4c5f78 35%, #8d9cb4 60%, #d9dde4 85%, #eceef1 100%); }
  .contact__panel { left: 547px; top: 0; width: 455px; height: 562px; background: var(--gold); }
  .contact__title { left: 638px; top: 92px; font-family: var(--head); font-weight: 800; font-size: 21px; color: var(--white); display: flex; align-items: center; gap: 16px; }
  .contact__title .brand__dot { background: var(--white); width: 40px; height: 40px; }
  .contact__info { left: 630px; top: 185px; color: var(--white); font-size: 16.5px; line-height: 25px; }
  .contact__company { font-family: var(--head); font-weight: 700; font-size: 15.5px; margin-bottom: 10px; }
  .contact__block { margin-top: 35px; }
</style>
</head>
<body>

<!-- Cover -->
<section class="slide slide--cover">
  <div class="photo cover__photo" role="img" aria-label="Photo of two smiling colleagues reviewing a document in a bright office"></div>
  <div class="brand cover__brand">
    <div class="brand__row"><span class="brand__dot"></span><span class="brand__name">Kalmora</span></div>
    <span class="brand__tag" style="margin-left:40px">NACHHALTIGKEITSBERATUNG</span>
  </div>
  <h1 class="abs cover__headline">WELCOME TO<br>KALMORA<br>SUSTAINABILITY<br>CONSULTING.</h1>
</section>

<!-- About us -->
<section class="slide slide--about">
  <div class="abs about__panel"></div>
  <p class="abs about__text">We support companies and<br>public institutions in anchoring<br>and expanding sustainability in<br>their homes - with the aim of<br>making them more attractive,<br>more sustainable and more<br>successful.</p>
  <div class="slide-title about__title"><span class="brand__dot"></span>ABOUT US</div>
  <div class="photo about__photo" role="img" aria-label="Photo of the three partners standing in front of a concrete wall"></div>
  <div class="abs about__accent"></div>
</section>

<!-- Team -->
<section class="slide slide--team">
  <div class="slide-title team__title"><span class="brand__dot"></span>TEAM</div>
  <article class="team-card" style="left:55px">
    <div class="team-card__photo" role="img" aria-label="Portrait photo of Dr Marta Wendel" style="background:linear-gradient(135deg,#d8d6d2,#b9a99b 60%,#3a3f4c)"></div>
    <div class="team-card__name">DR MARTA WENDEL</div>
    <div class="team-card__role">Managing Partners</div>
  </article>
  <article class="team-card" style="left:363px">
    <div class="team-card__photo" role="img" aria-label="Portrait photo of Dr Lena Ostrow" style="background:linear-gradient(135deg,#b8b4ad,#c9ad95 55%,#2f3440)"></div>
    <div class="team-card__name">DR LENA OSTROW</div>
    <div class="team-card__role">Managing Partners</div>
  </article>
  <article class="team-card" style="left:674px">
    <div class="team-card__photo" role="img" aria-label="Portrait photo of Dr Clara Brem-Hollis" style="background:linear-gradient(135deg,#c7cbc9,#b49684 55%,#2b2f3a)"></div>
    <div class="team-card__name">DR CLARA BREM-HOLLIS</div>
    <div class="team-card__role">Managing Partners</div>
  </article>
</section>

<!-- Data chart -->
<section class="slide slide--chart">
  <div class="slide-title chart__title"><span class="brand__dot"></span>DATA CHART</div>
  <h2 class="abs chart__heading">Lorem Ipsum is simply dummy text of the</h2>
  <p class="abs chart__copy">There are many variations of passages of Lorem Ipsum available, but the majority have suffered alteration in some form, by injected humour, or randomised words which don't look even slightly believable. If you are going to use a passage of Lorem Ipsum, you need to be sure there isn't anything embarrassing hidden in the middle of text. All the Lorem Ipsum generators on the Internet tend to repeat predefined chunks as necessary, making this the first true generator</p>
  <svg class="abs chart__svg" width="1002" height="562" viewBox="0 0 1002 562" aria-label="Column chart, January to April">
    <g stroke="var(--grid)" stroke-width="1">
      <line x1="387" y1="163" x2="962" y2="163"/>
      <line x1="387" y1="208" x2="962" y2="208"/>
      <line x1="387" y1="253" x2="962" y2="253"/>
      <line x1="387" y1="298" x2="962" y2="298"/>
      <line x1="387" y1="343" x2="962" y2="343"/>
      <line x1="387" y1="388" x2="962" y2="388"/>
      <line x1="387" y1="433" x2="962" y2="433"/>
      <line x1="387" y1="163" x2="387" y2="433"/>
      <line x1="962" y1="163" x2="962" y2="433"/>
    </g>
    <g font-family="Montserrat, Arial, sans-serif" font-size="19" fill="var(--axis)" text-anchor="end">
      <text x="383" y="170">60</text><text x="383" y="215">50</text><text x="383" y="260">40</text>
      <text x="383" y="305">30</text><text x="383" y="350">20</text><text x="383" y="395">10</text>
      <text x="383" y="440">0</text>
    </g>
    <rect x="442" y="253" width="18" height="180" fill="var(--jan-a)"/>
    <rect x="472" y="208" width="18" height="225" fill="var(--jan-b)"/>
    <rect x="576" y="383" width="18" height="50" fill="var(--feb-a)"/>
    <rect x="605" y="276" width="18" height="157" fill="var(--feb-b)"/>
    <rect x="699" y="172" width="18" height="261" fill="var(--mar-a)"/>
    <rect x="729" y="370" width="18" height="63" fill="var(--mar-b)"/>
    <rect x="822" y="199" width="18" height="234" fill="var(--apr-a)"/>
    <rect x="852" y="298" width="18" height="135" fill="var(--apr-b)"/>
    <g font-family="Montserrat, Arial, sans-serif" font-size="19" fill="var(--axis)" text-anchor="middle">
      <text x="475" y="468">JAN</text><text x="600" y="468">FEB</text>
      <text x="723" y="468">MAR</text><text x="846" y="468">APR</text>
    </g>
  </svg>
</section>

<!-- Timeline -->
<section class="slide slide--timeline">
  <svg class="abs timeline__svg" width="1002" height="562" viewBox="0 0 1002 562" aria-hidden="true">
    <defs>
      <radialGradient id="ringFill" cx="50%" cy="50%" r="50%">
        <stop offset="70%" stop-color="var(--ring)"/>
        <stop offset="100%" stop-color="var(--ring-soft)"/>
      </radialGradient>
    </defs>
    <g stroke="var(--ring)" stroke-width="1.5" stroke-dasharray="4 4" fill="none" opacity="0.8">
      <path d="M141 229 L319 337 L494 229 L670 337 L848 229"/>
      <line x1="141" y1="305" x2="141" y2="362"/><line x1="494" y1="305" x2="494" y2="362"/><line x1="848" y1="305" x2="848" y2="362"/>
      <line x1="319" y1="210" x2="319" y2="261"/><line x1="670" y1="210" x2="670" y2="261"/>
    </g>
    <g fill="var(--ring)">
      <circle cx="141" cy="362" r="6"/><circle cx="494" cy="362" r="6"/><circle cx="848" cy="362" r="6"/>
      <circle cx="319" cy="210" r="6"/><circle cx="670" cy="210" r="6"/>
    </g>
    <g id="nodes">
      <g transform="translate(141 229)"><circle r="76" fill="none" stroke="var(--ring)" stroke-dasharray="3 4" opacity="0.6"/><circle r="66" fill="url(#ringFill)"/><circle r="52" fill="#fff"/></g>
      <g transform="translate(319 337)"><circle r="76" fill="none" stroke="var(--ring)" stroke-dasharray="3 4" opacity="0.6"/><circle r="66" fill="url(#ringFill)"/><circle r="52" fill="#fff"/></g>
      <g transform="translate(494 229)"><circle r="76" fill="none" stroke="var(--ring)" stroke-dasharray="3 4" opacity="0.6"/><circle r="66" fill="url(#ringFill)"/><circle r="52" fill="#fff"/></g>
      <g transform="translate(670 337)"><circle r="76" fill="none" stroke="var(--ring)" stroke-dasharray="3 4" opacity="0.6"/><circle r="66" fill="url(#ringFill)"/><circle r="52" fill="#fff"/></g>
      <g transform="translate(848 229)"><circle r="76" fill="none" stroke="var(--ring)" stroke-dasharray="3 4" opacity="0.6"/><circle r="66" fill="url(#ringFill)"/><circle r="52" fill="#fff"/></g>
    </g>
    <g stroke="var(--leaf-green)" stroke-width="3" fill="none" stroke-linecap="round" stroke-linejoin="round">
      <!-- edit -->
      <path d="M128 220 h-6 v26 h26 v-8"/><path d="M134 240 l2 -7 l15 -15 l5 5 l-15 15 z"/>
      <!-- settings -->
      <circle cx="319" cy="337" r="8"/><circle cx="319" cy="337" r="17" stroke-dasharray="6 4"/>
      <!-- document -->
      <rect x="481" y="213" width="26" height="34" rx="2"/><line x1="487" y1="222" x2="501" y2="222"/><line x1="487" y1="230" x2="501" y2="230"/><line x1="487" y1="238" x2="497" y2="238"/>
      <!-- presentation board -->
      <rect x="658" y="320" width="26" height="20"/><path d="M663 335 l5 -5 l4 3 l7 -8"/><line x1="671" y1="340" x2="665" y2="355"/><line x1="671" y1="340" x2="677" y2="355"/>
      <!-- chat -->
      <path d="M836 215 h26 v18 h-14 l-7 6 v-6 h-5 z"/>
    </g>
    <g fill="var(--leaf-green)"><circle cx="842" cy="224" r="2"/><circle cx="849" cy="224" r="2"/><circle cx="856" cy="224" r="2"/></g>
  </svg>
  <div class="slide-title timeline__title"><span class="brand__dot"></span>TIMELINE</div>

  <div class="step" style="left:221px; top:54px"><div class="step__label">LOREM IPSUM</div><p class="step__copy">There are many variations of passages of Lorem Ipsum available, but the majority have suffered alteration in some form, by injected humour, or randomised words which don't look even slightly believable. If you are going to use a passage of Lorem Ipsum</p></div>
  <div class="step" style="left:572px; top:54px"><div class="step__label">LOREM IPSUM</div><p class="step__copy">There are many variations of passages of Lorem Ipsum available, but the majority have suffered alteration in some form, by injected humour, or randomised words which don't look even slightly believable. If you are going to use a passage of Lorem Ipsum</p></div>
  <div class="step" style="left:43px; top:403px"><div class="step__label">LOREM IPSUM</div><p class="step__copy">There are many variations of passages of Lorem Ipsum available, but the majority have suffered alteration in some form, by injected humour, or randomised words which don't look even slightly believable. If you are going to use a passage of Lorem Ipsum</p></div>
  <div class="step" style="left:396px; top:403px"><div class="step__label">LOREM IPSUM</div><p class="step__copy">There are many variations of passages of Lorem Ipsum available, but the majority have suffered alteration in some form, by injected humour, or randomised words which don't look even slightly believable. If you are going to use a passage of Lorem Ipsum</p></div>
  <div class="step" style="left:752px; top:403px"><div class="step__label">LOREM IPSUM</div><p class="step__copy">There are many variations of passages of Lorem Ipsum available, but the majority have suffered alteration in some form, by injected humour, or randomised words which don't look even slightly believable. If you are going to use a passage of Lorem Ipsum</p></div>
</section>

<!-- Contact -->
<section class="slide slide--contact">
  <div class="photo contact__photo" role="img" aria-label="Photo of three colleagues discussing work around a laptop at a meeting table"></div>
  <div class="abs contact__panel"></div>
  <div class="abs contact__title"><span class="brand__dot"></span>CONTACT</div>
  <div class="abs contact__info">
    <div class="contact__company">Kalmora Consulting GmbH</div>
    <div>Lindenhof Office Park</div>
    <div>Ahornweg 12</div>
    <div>60000 Musterstadt/ Frankfurt a. M</div>
    <div class="contact__block">Phone:</div>
    <div>+49 (0) 6100 – 555 0142</div>
    <div class="contact__block">Email:</div>
    <div>info@kalmora-consulting.example</div>
  </div>
</section>

</body>
</html>
```